Sales Flyer for Outdoor Kitchens

Looks to have a trifold flyer designed based off website content / projects. Use www.patiohearthcrafters.com for content

```html
<!DOCTYPE html>
<html lang="en">
<head>
<meta charset="utf-8">
<title>Patio Hearth Crafters – Trifold Flyer</title>
<link href="https://fonts.googleapis.com/css2?family=Montserrat:ital,wght@0,400;0,600;0,700;0,800;1,800&family=Open+Sans:wght@400;600&family=Caveat:wght@500&display=swap" rel="stylesheet">
<style>
:root{
  --blue:#1a62b8;
  --blue-dark:#0f4f9e;
  --green:#3aaa35;
  --ink:#1d1d1f;
  --grey:#4a4a4a;
  --paper:#ffffff;
  --mist:#eef1f4;
  --bg:#e7e7e7;
}
*{box-sizing:border-box;margin:0;padding:0}
html,body{width:803px;height:1200px;overflow:hidden;background:var(--bg)}
body{font-family:"Open Sans",Arial,sans-serif;color:var(--grey);position:relative}
.sheet{position:absolute;left:16px;width:771px;height:545px;background:var(--paper);overflow:hidden;box-shadow:0 2px 8px rgba(0,0,0,.18)}
.sheet-outside{top:40px}
.sheet-inside{top:615px}
.abs{position:absolute}
.photo{position:absolute}
.curves{position:absolute;left:0;top:0}
.eyebrow{font-family:"Montserrat",sans-serif;font-weight:600;font-size:7px;color:var(--blue)}
.section-title{font-family:"Montserrat",sans-serif;font-weight:800;font-size:14px;color:var(--ink);display:flex;align-items:center;gap:6px}
.section-title em{font-style:normal;color:var(--green)}
.section-title::after{content:"";width:30px;height:2px;background:var(--green)}
.body-copy{font-size:8.2px;line-height:1.28;color:var(--grey)}
.rule{height:1px;background:#d4d4d4}
/* contact */
.contact-pill{font-family:"Montserrat",sans-serif;font-weight:700;font-size:13px;color:#fff;background:var(--blue-dark);border:1.5px solid #6fa6e6;border-radius:4px;text-align:center;letter-spacing:.5px}
.contact-phone{font-family:"Montserrat",sans-serif;font-weight:700;font-size:23px;color:#fff;display:flex;align-items:center;gap:5px}
.contact-line{font-family:"Montserrat",sans-serif;font-size:9.5px;color:#fff;display:flex;align-items:center;gap:7px;line-height:1.15}
/* tagline */
.tag-script{font-family:"Caveat",cursive;font-size:30px;color:var(--ink)}
.tag-blue{font-family:"Montserrat",sans-serif;font-weight:800;font-size:24px;color:var(--blue)}
.tag-green{font-family:"Montserrat",sans-serif;font-weight:800;font-size:24px;color:var(--green)}
.tag-dark{font-family:"Montserrat",sans-serif;font-weight:400;font-size:24px;color:var(--ink)}
.url-pill{font-family:"Montserrat",sans-serif;font-weight:600;font-size:11px;color:#fff;border-radius:5px;text-align:center;line-height:22px;height:22px}
.url-blue{background:var(--blue)}
.url-green{background:var(--green)}
/* brand */
.brand{display:flex;align-items:center;gap:8px;font-family:"Montserrat",sans-serif;font-weight:700;font-size:14px;color:var(--blue)}
.brand-dot{width:14px;height:14px;border-radius:50%;background:var(--green)}
/* inside */
.services-tab-small{font-family:"Montserrat",sans-serif;font-size:11px;color:#fff;text-align:center}
.services-tab-title{font-family:"Montserrat",sans-serif;font-weight:800;font-size:20px;color:#fff;line-height:1;text-align:center}
.process-title{font-family:"Montserrat",sans-serif;font-weight:800;font-style:italic;font-size:16px;color:#fff;line-height:1.1;text-align:center}
.service-card{position:absolute;left:24px;top:95px;width:466px;height:428px;background:var(--paper);border-radius:18px}
.service{position:absolute;width:168px}
.service .thumb{height:74px;border-radius:8px}
.service h3{font-family:"Montserrat",sans-serif;font-weight:700;font-size:11px;color:var(--green);margin-top:12px;line-height:1.05}
.service p{font-size:8px;line-height:1.2;color:var(--grey)}
.info-col{position:absolute;left:529px;top:22px;width:220px}
.info-col h4{font-family:"Montserrat",sans-serif;font-weight:700;font-size:9px;color:var(--blue);margin-top:9px}
.info-col h4.dark{color:var(--ink);margin-top:5px}
.info-col p{font-size:7.3px;line-height:1.25;color:var(--grey)}
</style>
</head>
<body>

<!-- OUTSIDE SHEET -->
<section class="sheet sheet-outside" aria-label="Flyer outside">
  <div class="photo" style="left:257px;top:0;width:514px;height:330px;background:linear-gradient(160deg,#4f7a3a 0%,#6b4a2e 45%,#9a6a43 65%,#3f6b2f 100%)" role="img" aria-label="Photo of a cedar pavilion with seating and a fire table in a wooded backyard"></div>
  <div class="photo" style="left:0;top:320px;width:257px;height:225px;background:linear-gradient(170deg,#8a8f86 0%,#e9e6df 40%,#6d6a60 75%,#4a4a44 100%)" role="img" aria-label="Photo of a white pergola over an outdoor dining area"></div>

  <svg class="curves" width="771" height="545" viewBox="0 0 771 545" aria-hidden="true">
    <!-- left panel bottom curve -->
    <path d="M0 318 C80 300 170 300 257 318 L257 0 L0 0 Z" fill="#ffffff"/>
    <path d="M0 318 C80 300 170 300 257 318" fill="none" stroke="var(--green)" stroke-width="6"/>
    <!-- lower blue and light panels -->
    <path d="M257 345 C380 300 520 300 771 330 L771 545 L257 545 Z" fill="var(--blue)"/>
    <path d="M257 345 C380 300 520 300 771 330" fill="none" stroke="#ffffff" stroke-width="7"/>
    <path d="M257 338 C380 292 520 292 771 322" fill="none" stroke="var(--green)" stroke-width="4"/>
    <path d="M513 362 C600 338 690 338 771 352 L771 545 L513 545 Z" fill="var(--mist)"/>
    <!-- logo tab -->
    <path d="M529 0 L771 0 L771 113 L556 113 Q529 113 529 86 Z" fill="#ffffff" stroke="var(--green)" stroke-width="3"/>
  </svg>

  <div class="brand abs" style="left:555px;top:48px"><span class="brand-dot"></span>PATIO HEARTH CRAFTERS</div>

  <div class="abs" style="left:34px;top:18px;width:205px">
    <div class="eyebrow">What we do</div>
    <div class="section-title">WHO <em>WE ARE</em></div>
    <p class="body-copy" style="margin-top:8px">With over a decade of experience in the industry, Dale Whitmore, the owner and operator of PHC, has become a well-known name in the Houston area. His passion for outdoor living spaces, coupled with his keen eye for design and attention to detail, has led him to create some of the most stunning and functional outdoor spaces for his clients.</p>
    <div class="rule" style="margin:14px 0 12px"></div>
    <div class="section-title">OUR <em>MISSION</em></div>
    <p class="body-copy" style="margin-top:8px">At Patio Hearth Crafters, our mission is to redefine outdoor living by blending innovative design with unmatched craftsmanship. We strive to create spaces that not only meet but exceed your expectations. Our goal is to transform your outdoor area into a haven that reflects your personality and provides a seamless connection between nature and your home.</p>
  </div>

  <div class="contact-pill abs" style="left:293px;top:366px;width:184px;height:22px;line-height:19px">CONTACT</div>
  <div class="contact-phone abs" style="left:288px;top:392px">
    <svg width="14" height="18" viewBox="0 0 24 24" aria-hidden="true"><path fill="#fff" d="M6.6 10.8a15 15 0 0 0 6.6 6.6l2.2-2.2c.3-.3.7-.4 1-.2 1.1.4 2.3.6 3.6.6.6 0 1 .4 1 1V20c0 .6-.4 1-1 1A17 17 0 0 1 3 4c0-.6.4-1 1-1h3.5c.6 0 1 .4 1 1 0 1.3.2 2.5.6 3.6.1.3 0 .7-.2 1z"/></svg>
    555-014-2290
  </div>
  <div class="contact-line abs" style="left:292px;top:426px">
    <svg width="8" height="11" viewBox="0 0 24 24" aria-hidden="true"><path fill="#fff" d="M12 2a7 7 0 0 0-7 7c0 5 7 13 7 13s7-8 7-13a7 7 0 0 0-7-7zm0 9.5a2.5 2.5 0 1 1 0-5 2.5 2.5 0 0 1 0 5z"/></svg>
    <span>418 Cedar Bend Rd Ste 210<br>Brookfield, 77000, US</span>
  </div>
  <div class="contact-line abs" style="left:292px;top:458px">
    <svg width="10" height="10" viewBox="0 0 24 24" aria-hidden="true"><circle cx="12" cy="12" r="11" fill="#fff"/><path d="M6 8h12v8H6z M6 8l6 5 6-5" fill="none" stroke="var(--blue)" stroke-width="1.6"/></svg>
    DW@patiohearthcrafters.com
  </div>
  <div class="contact-line abs" style="left:292px;top:480px">
    <svg width="10" height="10" viewBox="0 0 24 24" aria-hidden="true"><circle cx="12" cy="12" r="11" fill="#fff"/><circle cx="12" cy="12" r="6" fill="none" stroke="var(--blue)" stroke-width="1.6"/><path d="M6 12h12M12 6v12" stroke="var(--blue)" stroke-width="1.4"/></svg>
    www.patiohearthcrafters.com
  </div>

  <div class="abs" style="left:513px;top:385px;width:258px;text-align:center;line-height:1">
    <div class="tag-script">Create</div>
    <div class="tag-blue">YOUR DREAM</div>
    <div class="tag-green">Backyard</div>
    <div class="tag-dark">With Us</div>
  </div>
  <div class="url-pill url-blue abs" style="left:544px;top:510px;width:196px">patiohearthcrafters.com</div>
</section>

<!-- INSIDE SHEET -->
<section class="sheet sheet-inside" aria-label="Flyer inside">
  <div class="abs" style="left:0;top:0;width:513px;height:545px;background:var(--blue)"></div>

  <svg class="curves" width="771" height="545" viewBox="0 0 771 545" aria-hidden="true">
    <path d="M0 0 L250 0 L222 78 Q216 92 200 90 L34 90 Q14 90 6 78 L0 70 Z" fill="var(--blue-dark)"/>
    <path d="M0 68 Q10 90 34 92 L200 92 Q218 92 224 76 L250 0" fill="none" stroke="#ffffff" stroke-width="3"/>
  </svg>

  <div class="abs" style="left:20px;top:18px;width:212px">
    <div class="services-tab-small">WHAT WE DO</div>
    <div class="services-tab-title">OUR TURNKEY<br>SERVICES</div>
  </div>
  <div class="process-title abs" style="left:270px;top:24px;width:230px">EFFECTIVE<br>PROCESS FOR GREAT<br>OUTCOMES</div>

  <div class="service-card"></div>

  <div class="service" style="left:60px;top:113px">
    <div class="thumb" style="background:linear-gradient(160deg,#3f6b34,#8b4a35 55%,#9a9a94)" role="img" aria-label="Photo of a brick outdoor kitchen with grill"></div>
    <h3>OUTDOOR KITCHENS</h3>
    <p>Culinary Excellence in Your Outdoor Sanctuary Welcome to Outdoor</p>
  </div>
  <div class="service" style="left:60px;top:246px">
    <div class="thumb" style="background:linear-gradient(160deg,#6e8fb0,#f1efea 45%,#6a5a4a)" role="img" aria-label="Photo of a white pavilion over a patio"></div>
    <h3>PAVILIONS, PATIOS &amp;<br>PERGOLAS</h3>
    <p>Pergolas and Patio Covers – Shaping Serenity in Your</p>
  </div>
  <div class="service" style="left:60px;top:390px">
    <div class="thumb" style="background:linear-gradient(160deg,#5b6e3c,#a99a86 50%,#e08a3a 62%,#7d6f60)" role="img" aria-label="Photo of a stone fire pit with seating wall"></div>
    <h3>FIRE PITS</h3>
    <p>Elevate Your Outdoor Space with Unique Fire Features At</p>
  </div>
  <div class="service" style="left:285px;top:113px">
    <div class="thumb" style="background:linear-gradient(180deg,#a9c7e6,#f2f2f2 45%,#38a8d8 75%,#6b7d5a)" role="img" aria-label="Photo of a backyard swimming pool beside a house"></div>
    <h3>POOLS</h3>
    <p>Our expert team will create a customized plan that brings together your</p>
  </div>
  <div class="service" style="left:285px;top:246px">
    <div class="thumb" style="background:linear-gradient(160deg,#1e3a22,#3f7a34 50%,#22402a)" role="img" aria-label="Photo of lush landscaping with garden lighting"></div>
    <h3>LANDSCAPING &amp;<br>LIGHTING</h3>
    <p>Design a captivating backyard oasis with our landscaping and lighting service, harmonizing</p>
  </div>

  <div class="photo" style="left:300px;top:415px;width:213px;height:130px;background:linear-gradient(170deg,#f3f3f1,#d9d6cf 55%,#9c9890)" role="img" aria-label="Photo of a covered patio with built-in outdoor kitchen"></div>
  <svg class="curves" width="771" height="545" viewBox="0 0 771 545" aria-hidden="true">
    <path d="M300 545 L300 470 Q310 415 380 412 L513 412 L513 400 L370 400 Q292 404 290 470 L290 545 Z" fill="var(--blue)"/>
    <path d="M296 545 L296 472 Q304 412 378 408 L513 408" fill="none" stroke="var(--green)" stroke-width="5"/>
  </svg>

  <div class="info-col">
    <div class="section-title">OUR <em>EXPERTISE</em></div>
    <h4 class="dark">Outdoor Living Spaces:</h4>
    <p>Our team specializes in designing outdoor living spaces that harmonize with your lifestyle, providing the perfect backdrop for relaxation and entertainment.</p>
    <h4>Patios:</h4>
    <p>Elevate your outdoor experience with a well-designed patio that seamlessly extends your living space into the open air. we tailor our designs to your unique preferences.</p>
    <h4>Pergolas:</h4>
    <p>Embrace the allure of outdoor elegance with our custom pergola designs. Whether you seek a cozy nook or a captivating focal point, our pergolas are crafted to elevate your outdoor aesthetic.</p>
    <h4>Fire Features:</h4>
    <p>Our fire features combine style with ambiance. We offer everything from eye-catching fireplaces to fire pits that promise to beckon a crowd.</p>
    <div class="rule" style="margin:12px 0 10px"></div>
    <div class="section-title">OUR <em>VALUES</em></div>
    <p style="font-size:8.3px;margin-top:5px">We perform complete turnkey services</p>
    <h4>Passion:</h4>
    <p>We're driven by a deep passion for outdoor design, and it is reflected in every project. Our commitment to excellence is fueled by our genuine love for creating outdoor spaces that enhance the quality of life.</p>
    <h4>Attention to Detail:</h4>
    <p>Every element matters. We approach each design with meticulous attention to detail, ensuring that every aspect contributes to the overall aesthetic and functionality of your outdoor space</p>
    <h4>Client-Centric Approach:</h4>
    <p>Your vision is our priority. We believe in collaborative design, working closely with you to understand your preferences and lifestyle, and translating them into a personalized outdoor oasis.</p>
  </div>
  <div class="url-pill url-green abs" style="left:548px;top:508px;width:196px">patiohearthcrafters.com</div>
</section>

</body>
</html>
```